Harborline Stay Collective Business Card Design

Design a business card for Harborline Stay Collective. Look at the website for colors and reference. Card should have logo, name, title, office number, mobile number, email, URL and a tagline like, "Luxury Hotel & Resort Email Marketing" (This might change).

https://www.harborlinestaycollective.net

The rest I will leave up to your imagination.

Contact Information for Business Card

Logo, name, title, office number, mobile number, email, URL and a tagline like, "Luxury Hotel & Resort Email Marketing" (This might change).

```html
<!DOCTYPE html>
<html lang="en">
<head>
<meta charset="utf-8">
<title>Harborline Stay Collective – Business Card</title>
<link href="https://fonts.googleapis.com/css2?family=Questrial&family=Montserrat:ital,wght@1,600&display=swap" rel="stylesheet">
<style>
  :root {
    --backdrop: #e8e8e8;
    --orange: #f47420;
    --white: #ffffff;
    --ink: #111111;
    --shadow: 0 3px 8px rgba(0,0,0,0.18);
  }
  * { margin: 0; padding: 0; box-sizing: border-box; }
  html, body { width: 1200px; height: 1200px; overflow: hidden; }
  body {
    background: var(--backdrop);
    position: relative;
    font-family: "Questrial", "Century Gothic", sans-serif;
  }
  .card {
    position: absolute;
    left: 156px;
    width: 888px;
    height: 520px;
    background: var(--orange);
    box-shadow: var(--shadow);
    overflow: hidden;
  }
  .card--front { top: 61px; }
  .card--back { top: 611px; }

  .brand-panel {
    position: absolute;
    left: 0; top: 0;
    width: 235px; height: 100%;
    background: var(--white);
  }
  .brand-vertical {
    position: absolute;
    left: 117px; top: 260px;
    transform: translate(-50%, -50%) rotate(-90deg);
    color: var(--ink);
    text-align: center;
    white-space: nowrap;
    line-height: 1;
  }
  .brand-vertical .brand-main { display: block; font-size: 52px; letter-spacing: 1px; }
  .brand-vertical .brand-sub { display: block; font-size: 24px; letter-spacing: 4px; margin-top: 8px; }

  .accent-bar {
    position: absolute;
    left: 262px; top: 0;
    width: 31px; height: 273px;
    background: var(--ink);
  }

  .identity {
    position: absolute;
    right: 94px; top: 114px;
    color: var(--white);
    white-space: nowrap;
  }
  .identity .person {
    font-family: "Montserrat", sans-serif;
    font-style: italic;
    font-weight: 600;
    font-size: 35px;
  }
  .identity .divider { font-size: 26px; margin: 0 4px 0 6px; }
  .identity .role { font-size: 20px; }

  .contacts {
    position: absolute;
    right: 84px; top: 252px;
    list-style: none;
    color: var(--white);
    font-size: 21px;
    text-align: right;
  }
  .contacts li {
    display: flex;
    justify-content: flex-end;
    align-items: center;
    height: 41px;
  }
  .contacts svg { width: 14px; height: 14px; margin-left: 12px; fill: var(--white); }

  .brand-centered {
    position: absolute;
    left: 50%; top: 50%;
    transform: translate(-50%, -50%);
    color: var(--white);
    text-align: center;
    white-space: nowrap;
    line-height: 1;
  }
  .brand-centered .brand-main { display: block; font-size: 66px; letter-spacing: 2px; }
  .brand-centered .brand-sub { display: block; font-size: 28px; letter-spacing: 6px; margin-top: 10px; }
</style>
</head>
<body>

<section class="card card--front">
  <div class="brand-panel">
    <div class="brand-vertical">
      <span class="brand-main">HARBORLINE</span>
      <span class="brand-sub">STAY COLLECTIVE</span>
    </div>
  </div>
  <div class="accent-bar"></div>

  <p class="identity">
    <span class="person">Daniel Reeve</span><span class="divider">/</span><span class="role">Founder</span>
  </p>

  <ul class="contacts">
    <li>033 2417 6630
      <svg viewBox="0 0 24 24" aria-hidden="true"><path d="M6.6 10.8a15.1 15.1 0 0 0 6.6 6.6l2.2-2.2c.3-.3.7-.4 1-.2 1.1.4 2.3.6 3.6.6.6 0 1 .4 1 1V20c0 .6-.4 1-1 1C10.6 21 3 13.4 3 4c0-.6.4-1 1-1h3.5c.6 0 1 .4 1 1 0 1.3.2 2.5.6 3.6.1.3 0 .7-.2 1z"/></svg>
    </li>
    <li>8561 904 318
      <svg viewBox="0 0 24 24" aria-hidden="true"><path d="M8 1h8a2 2 0 0 1 2 2v18a2 2 0 0 1-2 2H8a2 2 0 0 1-2-2V3a2 2 0 0 1 2-2zm0 3v14h8V4zm4 15.5a1.2 1.2 0 1 0 0 2.4 1.2 1.2 0 0 0 0-2.4z"/></svg>
    </li>
    <li>info@harborlinestaycollective.net
      <svg viewBox="0 0 24 24" aria-hidden="true"><path d="M2 5h20v2l-10 6L2 7zm0 4.3 10 6 10-6V19H2z"/></svg>
    </li>
    <li>www.harborlinestaycollective.net
      <svg viewBox="0 0 24 24" aria-hidden="true"><path d="M12 2a10 10 0 1 0 0 20 10 10 0 0 0 0-20zm6.9 6h-3a15.7 15.7 0 0 0-1.4-3.6A8 8 0 0 1 18.9 8zM12 4c.8 1.2 1.5 2.5 1.9 4h-3.8c.4-1.5 1.1-2.8 1.9-4zM4.3 14a8 8 0 0 1 0-4h3.4a16.5 16.5 0 0 0 0 4zm.8 2h3a15.7 15.7 0 0 0 1.4 3.6A8 8 0 0 1 5.1 16zm3-8h-3a8 8 0 0 1 4.4-3.6A15.7 15.7 0 0 0 8.1 8zM12 20c-.8-1.2-1.5-2.5-1.9-4h3.8c-.4 1.5-1.1 2.8-1.9 4zm2.3-6H9.7a14.7 14.7 0 0 1 0-4h4.6a14.7 14.7 0 0 1 0 4zm.2 5.6a15.7 15.7 0 0 0 1.4-3.6h3a8 8 0 0 1-4.4 3.6zm1.8-5.6a16.5 16.5 0 0 0 0-4h3.4a8 8 0 0 1 0 4z"/></svg>
    </li>
  </ul>
</section>

<section class="card card--back">
  <div class="brand-centered">
    <span class="brand-main">HARBORLINE</span>
    <span class="brand-sub">STAY COLLECTIVE</span>
  </div>
</section>

</body>
</html>
```